Oil and Gas Exploration and Production company needs a business card design

We need a business card design using our logo and colors in the logo. We want a mainstream design.

```html
<!DOCTYPE html>
<html lang="en">
<head>
<meta charset="utf-8">
<title>Meridian Oil &amp; Gas – Business Card</title>
<link rel="stylesheet" href="https://fonts.googleapis.com/css2?family=Lato:wght@400;700;900&display=swap">
<style>
  :root {
    --stage: #2b2b2b;
    --card-dark: #231f20;
    --card-light: #ffffff;
    --gold: #b8902f;
    --ink: #111111;
    --text: #222222;
    --rule: #333333;
  }
  * { box-sizing: border-box; margin: 0; padding: 0; }
  html, body { width: 1200px; height: 997px; overflow: hidden; }
  body {
    background: var(--stage);
    font-family: "Lato", Arial, sans-serif;
    display: flex;
    align-items: center;
    justify-content: center;
    gap: 40px;
  }
  .card {
    position: relative;
    width: 540px;
    height: 310px;
    overflow: hidden;
    box-shadow: 0 10px 30px rgba(0,0,0,.45);
  }
  /* Back */
  .card--back {
    background: var(--card-dark);
    display: flex;
    align-items: center;
    justify-content: center;
    gap: 16px;
  }
  .back-mark {
    width: 34px; height: 34px;
    border: 3px solid var(--gold);
    border-radius: 50%;
  }
  .back-name {
    color: var(--gold);
    font-weight: 900;
    font-size: 46px;
    letter-spacing: 1px;
  }
  /* Front */
  .card--front { background: var(--card-light); }
  .brand {
    position: absolute;
    left: 170px; top: 48px;
    display: flex; align-items: center; gap: 10px;
  }
  .brand-mark {
    width: 22px; height: 22px;
    background: var(--ink);
    border-radius: 50%;
  }
  .brand-name {
    color: var(--ink);
    font-weight: 900;
    font-size: 38px;
    line-height: 1;
  }
  .brand-rule {
    position: absolute;
    left: 170px; right: 36px; top: 110px;
    border-top: 1px solid var(--rule);
  }
  .person {
    position: absolute;
    left: 34px; top: 148px;
  }
  .person-name {
    color: var(--gold);
    font-weight: 700;
    font-size: 15px;
    letter-spacing: .5px;
    display: flex; align-items: center; gap: 6px;
  }
  .person-name::after {
    content: "";
    width: 70px;
    border-top: 1px solid var(--rule);
  }
  .person-title { font-size: 12px; color: var(--text); }
  .contacts {
    position: absolute;
    left: 34px; top: 196px;
    list-style: none;
  }
  .contact {
    display: flex; align-items: center; gap: 12px;
    font-size: 13px; color: var(--text);
    margin-bottom: 9px;
  }
  .contact-icon {
    width: 16px; height: 16px;
    border-radius: 50%;
    background: var(--gold);
    display: flex; align-items: center; justify-content: center;
  }
  .address {
    position: absolute;
    right: 30px; top: 196px;
    text-align: right;
    color: var(--gold);
    font-size: 11px;
    line-height: 1.3;
  }
  .footer-shape { position: absolute; left: 0; bottom: 0; }
  .website {
    position: absolute;
    right: 30px; bottom: 44px;
    color: #fff;
    font-weight: 700;
    font-size: 13px;
    letter-spacing: .5px;
  }
</style>
</head>
<body>
  <section class="card card--back" aria-label="Card back">
    <span class="back-mark"></span>
    <span class="back-name">Meridian</span>
  </section>

  <section class="card card--front" aria-label="Card front">
    <div class="brand">
      <span class="brand-mark"></span>
      <span class="brand-name">Meridian Oil &amp; Gas</span>
    </div>
    <div class="brand-rule"></div>

    <div class="person">
      <p class="person-name">DALE MORGAN</p>
      <p class="person-title">Vice President Operations</p>
    </div>

    <ul class="contacts">
      <li class="contact">
        <span class="contact-icon"><svg width="9" height="9" viewBox="0 0 10 10"><path d="M2 1l2 2-1 1.5c.6 1.2 1.3 1.9 2.5 2.5L7 6l2 2-1.2 1.5C4.5 9.2 .8 5.5.5 2.2z" fill="#fff"/></svg></span>
        0161 555 0142
      </li>
      <li class="contact">
        <span class="contact-icon"><svg width="8" height="10" viewBox="0 0 8 10"><rect x="1" y=".5" width="6" height="9" rx="1" fill="none" stroke="#fff"/><circle cx="4" cy="8" r=".6" fill="#fff"/></svg></span>
        817-555-0199
      </li>
      <li class="contact">
        <span class="contact-icon"><svg width="10" height="8" viewBox="0 0 10 8"><rect x=".5" y=".5" width="9" height="7" fill="none" stroke="#fff"/><path d="M.5.5L5 4.5 9.5.5" fill="none" stroke="#fff"/></svg></span>
        dale@meridianoilgas.com
      </li>
    </ul>

    <p class="address">2400 W Harbor Ave. Suite 110<br>Fort Worth, TX 76109</p>

    <svg class="footer-shape" width="540" height="90" viewBox="0 0 540 90" aria-hidden="true">
      <path d="M0 62 H270 C285 62 285 44 305 44 H540 V54 H310 C295 54 292 70 275 70 H0 Z" fill="var(--ink)"/>
      <path d="M275 70 C292 70 295 28 320 28 H540 V90 H0 V80 H275 Z" fill="var(--gold)"/>
      <rect x="0" y="70" width="280" height="6" fill="var(--card-light)"/>
    </svg>
    <p class="website">www.meridianoilgas.com</p>
  </section>
</body>
</html>
```